Preschool Website

Looking to have a one page splash with a contact us form that uses some kind of verification to keep bots from filling out the form. We would like for it to be dynamic for both mobile and desktop. Would like to have it show up in search engines for preschool in are area. Would like to include a link to the website are current parents use for payment information.

Target Market(s)

Young Adults with Childrens

Industry/Entity Type

Preschool

Coding

Coded - Design and coding required

Number of Pages Required

1 page

Colors

Designer to choose colors to be used in the design.

Requirements
Must have
• Searchable in Findlo
• Contact us form
• Name
• Phone
• Email
• Message box
• Form must have code entered to submit to prevent junk emails
• Link to the website we use for parents to make payments
• our phone and address clickable on device to make call or map on phone
Should not have
• more then one page

```html
<!DOCTYPE html>
<html lang="en">
<head>
<meta charset="utf-8">
<title>Little Sprout Early Learning Academy</title>
<link href="https://fonts.googleapis.com/css2?family=Lora:ital,wght@0,400;0,700;1,400&family=Poppins:wght@400&display=swap" rel="stylesheet">
<style>
  :root {
    --cream: #fff9e3;
    --orange: #f48a45;
    --green: #7edc0b;
    --navy: #1f3e66;
    --navy-text: #1e3a5c;
    --yellow: #ffd100;
    --pale-yellow: #fbf2a8;
    --cyan: #08dcd4;
    --ink: #3a3530;
    --footer: #1a1a1a;
    --white: #ffffff;
  }
  * { box-sizing: border-box; margin: 0; padding: 0; }
  html, body { width: 1200px; height: 1013px; overflow: hidden; background: var(--cream); }
  .page { position: relative; width: 1200px; height: 1013px; overflow: hidden; font-family: "Lora", serif; }
  .backdrop { position: absolute; inset: 0; }
  .brand {
    position: absolute; left: 20px; top: 280px; width: 420px;
    text-align: center; color: var(--navy-text);
    font-family: "Lora", serif; font-weight: 700; font-size: 42px; line-height: 53px; letter-spacing: 1px;
  }
  .welcome { position: absolute; left: 53px; top: 484px; width: 430px; }
  .welcome h1 { font-weight: 400; font-size: 31px; color: #2b2723; letter-spacing: .3px; }
  .welcome p {
    margin-top: 22px; width: 420px; font-style: italic; font-size: 13.4px; line-height: 23.2px;
    color: var(--ink); text-align: justify;
  }
  .contact-form { position: absolute; left: 625px; top: 387px; width: 277px; }
  .field {
    display: block; width: 276px; height: 44px; margin-bottom: 7px; border: none; background: var(--white);
    padding: 0 14px; font-family: "Lora", serif; font-size: 14px; color: #333;
  }
  .field::placeholder { color: #333; }
  .verify { display: flex; gap: 7px; }
  .captcha {
    width: 105px; height: 44px; background: var(--white); display: flex; align-items: center; justify-content: center; gap: 5px;
    font-family: "Lora", serif; font-weight: 700; font-size: 18px;
  }
  .captcha span:nth-child(1) { color: #1e2d50; transform: rotate(-12deg); }
  .captcha span:nth-child(2) { color: #111; transform: translateY(4px); }
  .captcha span:nth-child(3) { color: #3d2a14; transform: rotate(10deg); }
  .captcha span:nth-child(4) { color: #355c2a; transform: translateY(5px); }
  .captcha span:nth-child(5) { color: #2a6e5a; transform: rotate(-8deg) translateY(-3px); }
  .verify .field { width: 164px; }
  .submit {
    position: absolute; left: 166px; top: 257px; width: 111px; height: 43px; border: none;
    background: var(--orange); color: var(--white); font-family: "Lora", serif; font-size: 18px;
  }
  .action {
    position: absolute; display: flex; align-items: center; justify-content: center; text-align: center;
    color: var(--white); font-style: italic; font-size: 25px; line-height: 31px; text-decoration: none;
  }
  .action svg { position: absolute; inset: 0; width: 100%; height: 100%; }
  .action span { position: relative; }
  .action-call { left: 74px; top: 807px; width: 247px; height: 105px; }
  .action-map { left: 367px; top: 793px; width: 236px; height: 141px; }
  .action-portal { left: 641px; top: 807px; width: 247px; height: 105px; }
  .action-social { left: 904px; top: 816px; width: 185px; height: 112px; }
  .site-footer {
    position: absolute; left: 0; top: 936px; width: 1200px; height: 77px; background: var(--footer);
    color: #eee; font-family: "Poppins", sans-serif; font-size: 13.5px; text-align: center; line-height: 77px;
  }
</style>
</head>
<body>
<div class="page">
  <svg class="backdrop" width="1200" height="936" viewBox="0 0 1200 936">
    <defs>
      <linearGradient id="photoTone" x1="0" y1="0" x2="1" y2="1">
        <stop offset="0" stop-color="#e9e6dc"/>
        <stop offset=".45" stop-color="#d8c7b0"/>
        <stop offset="1" stop-color="#7fb9c9"/>
      </linearGradient>
    </defs>
    <rect x="0" y="0" width="1200" height="936" fill="url(#photoTone)" role="img" aria-label="Photo of smiling children playing in a bright classroom"/>
    <path d="M1028 700 C1060 600 1130 530 1200 506 V936 H1028 Z" fill="var(--pale-yellow)"/>
    <circle cx="780" cy="574" r="260" fill="var(--navy)" opacity=".93"/>
    <path d="M560 600 C620 690 690 735 760 745 C860 755 960 690 1050 688 C1120 686 1170 700 1200 708 V936 H560 Z" fill="var(--green)"/>
    <path d="M0 0 H345 C385 110 455 210 495 340 C535 470 565 560 615 630 L600 650 C550 570 520 470 480 340 C440 210 370 110 330 0 Z" fill="var(--orange)"/>
    <path d="M0 0 H315 C355 110 425 210 465 340 C505 470 540 565 600 640 C645 700 700 745 760 760 C860 782 960 722 1050 712 C1120 706 1170 800 1200 936 H0 Z" fill="var(--cream)"/>
    <rect x="0" y="0" width="300" height="270" fill="#f3e6c8" opacity=".55" role="img" aria-label="Faded photo of a child with painted hands"/>
  </svg>

  <div class="brand">LITTLE SPROUT<br>EARLY LEARNING<br>ACADEMY</div>

  <section class="welcome">
    <h1>WELCOME TO OUR SCHOOL</h1>
    <p>We are a locally owned and operated early education school serving our community through individual relationships with children and families, accredited play-based learning, and a comprehensive, research-based curriculum that promotes exploration and discovery as a way of learning, enabling children to develop confidence, creativity, and lifelong critical thinking skills! Please take a moment to visit our Friendbook page to see examples of our work with children and families and schedule a tour today to experience our classrooms and teachers in action. We look forward to welcoming you into our family!</p>
  </section>

  <form class="contact-form">
    <input class="field" type="text" placeholder="Name :">
    <input class="field" type="tel" placeholder="Phone :">
    <input class="field" type="email" placeholder="Email :">
    <input class="field" type="text" placeholder="Message :">
    <div class="verify">
      <div class="captcha" aria-label="Verification code"><span>Q</span><span>L</span><span>8</span><span>9</span><span>Z</span></div>
      <input class="field" type="text" placeholder="Type the Word:">
    </div>
    <button class="submit" type="submit">Submit</button>
  </form>

  <a class="action action-call" href="#">
    <svg viewBox="0 0 247 105"><ellipse cx="123.5" cy="52.5" rx="123" ry="52" fill="var(--yellow)"/>
      <path d="M40 20 C30 22 26 34 32 50 C40 70 56 82 72 86 C80 88 86 82 84 76 L78 66 C76 62 70 62 66 66 L62 70 C52 64 46 56 42 46 L46 42 C50 38 50 32 46 30 Z" fill="#fff" opacity=".28"/></svg>
    <span>Call Us Now!</span>
  </a>
  <a class="action action-map" href="#">
    <svg viewBox="0 0 236 141"><g fill="var(--cyan)">
      <circle cx="60" cy="60" r="48"/><circle cx="115" cy="45" r="42"/><circle cx="170" cy="55" r="45"/>
      <circle cx="195" cy="85" r="38"/><circle cx="130" cy="95" r="45"/><circle cx="55" cy="95" r="38"/>
      <path d="M150 120 L140 141 L175 118 Z"/></g>
      <path d="M38 30 C20 30 10 44 12 58 C14 74 38 104 38 104 C38 104 62 74 64 58 C66 44 56 30 38 30 Z M38 46 A10 10 0 1 1 37.9 46 Z" fill="#fff" opacity=".3" fill-rule="evenodd"/></svg>
    <span>Our Location</span>
  </a>
  <a class="action action-portal" href="#">
    <svg viewBox="0 0 247 105"><ellipse cx="123.5" cy="52.5" rx="123" ry="52" fill="var(--orange)"/>
      <text x="28" y="95" font-family="Lora, serif" font-weight="700" font-size="100" fill="#fff" opacity=".25">$</text></svg>
    <span>Click for Parent<br>Portal</span>
  </a>
  <a class="action action-social" href="#">
    <svg viewBox="0 0 185 112"><g fill="var(--cyan)">
      <circle cx="40" cy="50" r="38"/><circle cx="90" cy="38" r="36"/><circle cx="140" cy="45" r="38"/>
      <circle cx="150" cy="72" r="32"/><circle cx="95" cy="75" r="35"/><circle cx="40" cy="72" r="32"/>
      <path d="M110 95 L102 112 L130 96 Z"/></g></svg>
    <span>Friendbook</span>
  </a>

  <footer class="site-footer">© Copyright 2020 Little Sprout Early Learning Academy.&nbsp; All Rights Reserved</footer>
</div>
</body>
</html>
```